Floristry Business Card Design Project

I have a logo now and am looking to incorporate this into a business card. I would like a double sided business card. I would like one side to be decorative so that it blends well when included with floral arrangements and that can also be used as the front of a card and the other side will contain the business details. The font on the business details side should be clear although some decorative font would be ok. I have included the logo files for use in the business card design.

Feel free to break up the logo and use certain aspects of it in the design. Really looking for something that stands out and that is really creative.

Industry/Entity Type

Floral

Requirements
Should not have
• Nothing tacky or corny. The logo should be clearly read (perhaps a background colour).

```html
<!DOCTYPE html>
<html lang="en">
<head>
<meta charset="utf-8">
<title>Petal Lane – Business Card</title>
<link href="https://fonts.googleapis.com/css2?family=Open+Sans:wght@400;600;700&family=Pinyon+Script&family=Patrick+Hand+SC&display=swap" rel="stylesheet">
<style>
  :root {
    --leaf: #8cc63f;
    --leaf-mid: #a9d66a;
    --leaf-pale: #e8f4d6;
    --sun: #f2e600;
    --ink: #111111;
    --paper: #ffffff;
    --band: #050505;
    --brand: #7fb98a;
    --icon-blue: #5aa7e6;
    --icon-sky: #bfe0f5;
    --icon-deep: #3d8ccc;
    --social: #dcdcdc;
  }
  * { box-sizing: border-box; margin: 0; padding: 0; }
  html, body {
    width: 934px; height: 1200px; overflow: hidden;
    background: var(--paper);
    font-family: "Open Sans", Arial, sans-serif;
    color: var(--ink);
  }
  .side-label {
    position: absolute; left: 0; width: 934px;
    text-align: center;
    font-family: "Open Sans", Arial, sans-serif;
    font-weight: 700; font-size: 32px;
  }
  .side-label--front { top: 0; }
  .side-label--back { top: 622px; }

  .card {
    position: absolute; left: 41px; width: 852px; height: 453px;
    overflow: hidden;
    background:
      radial-gradient(ellipse 340px 300px at 0% 10%, var(--paper) 0%, rgba(255,255,255,.85) 35%, rgba(255,255,255,0) 100%),
      linear-gradient(100deg, var(--paper) 0%, var(--leaf-pale) 12%, var(--leaf-mid) 32%, var(--leaf) 55%, var(--leaf) 100%);
  }
  .card--front { top: 65px; }
  .card--back { top: 700px; }

  .card__top-rule {
    position: absolute; left: 0; top: 0; width: 100%; height: 7px;
    background: var(--sun);
  }
  .card__footer {
    position: absolute; left: 0; bottom: 0; width: 100%; height: 42px;
    background: var(--band);
    border-top: 4px solid var(--sun);
    font-family: "Patrick Hand SC", "Comic Sans MS", cursive;
    color: var(--paper); font-size: 19px; letter-spacing: .5px;
  }
  .footer-item {
    position: absolute; top: 4px; display: flex; align-items: center; gap: 8px;
    height: 32px;
  }
  .footer-item svg { display: block; }
  .social-mark {
    width: 28px; height: 28px; background: var(--social); border-radius: 3px;
  }

  /* Front */
  .logo-tile {
    position: absolute; left: 66px; top: 97px; width: 198px; height: 198px;
    background: var(--paper);
    transform: rotate(45deg);
    box-shadow: 2px 3px 8px rgba(0,0,0,.25);
  }
  .brand-name {
    position: absolute; left: 65px; top: 182px; width: 200px;
    text-align: center;
    font-family: "Open Sans", Arial, sans-serif;
    font-size: 19px; font-weight: 400; letter-spacing: 3px;
    color: var(--brand); text-transform: uppercase;
  }
  .holder-name {
    position: absolute; left: 372px; top: 136px;
    font-family: "Pinyon Script", "Brush Script MT", cursive;
    font-size: 78px; font-weight: 400; line-height: 1; color: var(--ink);
  }
  .name-rule {
    position: absolute; left: 290px; top: 233px; width: 540px; height: 2px;
    background: linear-gradient(90deg, rgba(255,255,255,0), rgba(255,255,255,.9) 40%, rgba(120,160,60,.6) 70%, rgba(255,255,255,0));
  }
  .holder-phone {
    position: absolute; left: 409px; top: 247px;
    font-size: 31px; color: var(--ink);
  }

  /* Back */
  .pattern-field {
    position: absolute; inset: 7px 0 42px 0;
    background: radial-gradient(circle at 50% 50%, rgba(255,255,255,.10), rgba(255,255,255,0) 70%);
  }
  .department {
    position: absolute; right: 386px; top: 168px;
    text-align: right; font-size: 25px; line-height: 37px; color: var(--ink);
  }
  .divider {
    position: absolute; left: 494px; top: 84px; width: 3px; height: 300px;
    background: linear-gradient(180deg, rgba(255,255,255,0), rgba(255,255,255,.9) 30%, rgba(90,130,40,.5) 60%, rgba(255,255,255,0));
  }
  .offices { position: absolute; left: 523px; top: 124px; color: var(--paper); }
  .office__title { font-size: 24px; font-weight: 700; line-height: 32px; }
  .office__lines {
    list-style: none; margin: 6px 0 22px 4px;
    font-size: 13px; font-weight: 600; line-height: 19px;
  }
  .office__lines li { padding-left: 14px; position: relative; }
  .office__lines li:first-child::before {
    content: ""; position: absolute; left: 0; top: 7px;
    width: 5px; height: 5px; border-radius: 50%; background: var(--paper);
  }
</style>
</head>
<body>
  <h2 class="side-label side-label--front">the front</h2>

  <section class="card card--front">
    <div class="card__top-rule"></div>
    <div class="logo-tile"></div>
    <div class="brand-name">Petal Lane</div>
    <h1 class="holder-name">Your Name</h1>
    <div class="name-rule"></div>
    <p class="holder-phone">Phone: 1234567890</p>
    <footer class="card__footer">
      <div class="footer-item" style="left:6px">
        <svg width="30" height="28" viewBox="0 0 30 28" aria-hidden="true">
          <path d="M15 2 L28 14 L24 14 L24 26 L6 26 L6 14 L2 14 Z" fill="var(--icon-blue)"/>
          <rect x="12" y="17" width="6" height="9" fill="var(--paper)"/>
        </svg>
        <span>www.yoursite.com</span>
      </div>
      <div class="footer-item" style="left:556px">
        <svg width="30" height="26" viewBox="0 0 30 26" aria-hidden="true">
          <rect x="2" y="5" width="26" height="18" rx="2" fill="var(--icon-sky)"/>
          <path d="M2 7 L15 16 L28 7" fill="none" stroke="var(--icon-deep)" stroke-width="2"/>
        </svg>
        <span>your@yoursite.com</span>
      </div>
    </footer>
  </section>

  <h2 class="side-label side-label--back">back</h2>

  <section class="card card--back">
    <div class="card__top-rule"></div>
    <div class="pattern-field" role="img" aria-label="Faint repeating floral pattern"></div>
    <p class="department">Your Department / Section:<br>Design Grafis</p>
    <div class="divider"></div>
    <div class="offices">
      <h3 class="office__title">The Main Office :</h3>
      <ul class="office__lines">
        <li>Department 415</li>
        <li>PO Box 20418, Larkmoor, CA 90412</li>
      </ul>
      <h3 class="office__title">Branch Office :</h3>
      <ul class="office__lines">
        <li>Department 215</li>
        <li>PO Box 20426, Larkmoor, CA 90415</li>
      </ul>
    </div>
    <footer class="card__footer">
      <div class="footer-item" style="left:30px">
        <span class="social-mark"></span><span>Your Microblog</span>
      </div>
      <div class="footer-item" style="left:345px">
        <span class="social-mark"></span><span>Your Profile</span>
      </div>
      <div class="footer-item" style="left:680px">
        <span class="social-mark"></span><span>Your Photos</span>
      </div>
    </footer>
  </section>
</body>
</html>
```